Small and passionate motorcycle workshop requires a business card that kicks butt!

I'm Darren, I'm passionate about my motorcycles, I'm passionate about my desert racing and I'm a passionate motorcycle technician, that's why I started my own motorcycle workshop: 'Rivo Tanza'.
I started my workshop in my dining room and it’s eventually moved into a newly renovated shed that my Grandpa built with his own two hands in the early 1960's. To the customer the shed looks like a farm shed on my property, however the inside is ready for open heart surgery on their "Baby" which could be a late model sports bike, a highway cruiser, an old four-wheeler or an off road desert racing weapon!
This business is my own, I've built it from my dining room floor and I'm deeply passionate about it.
I need a professional business card and logo which looks like a heart and soul is intermingled through it because that is how my business is run. Rivo Tanza may have started from my dining room but it has always been professionally run and I have always put my passion into the bikes I've worked on.

-The text only logo needs to be comprised of 'Rivo Tanza'
-The business card will be double sided

And I do realise it will be a hard task to make something look professional and personal at the same time...however there are some very talented people in this world and I can’t wait to see what you create!

I've added some logo/designs that I'm fond of.

Industry/Entity Type

Racing

Requirements
Must have
• My name - Darren Pulkett
My Qualification - Qualified Motorcycle Technician
Ph - 0471 582 930
Email - rivotanza@quillmail.example
Address - 17 Bellbrook Lane, Williamstown, SA
ABN - 61 804 392 117 (plesase include the 'ABN' part
Needs to include these dot points:
-Servicing
-Repairs
-All makes/models
-Weekends by appt.
-Pick-up/delivery available
Nice to have
• I like the idea of calling myself a "Qualified and Passionate Motorcycle Technician". If the card does not come across that it’s a passionate business I'd like this line to be used on the card near my name.

One idea I like would include having the text only logo on the front being quite bold and contrasted to the background, then having my name and number smaller underneath somewhere. I'm very open to whatever comes my way so I'm look forward to seeing some sweet ideas!

```html
<!DOCTYPE html>
<html lang="en">
<head>
<meta charset="utf-8">
<title>Rivo Tanza – Business Card</title>
<link rel="stylesheet" href="https://fonts.googleapis.com/css2?family=Varela+Round&display=swap">
<style>
  :root {
    --stage: #6a6a6a;
    --card: #2d2d2d;
    --band: #444444;
    --band-edge: #3a3a3a;
    --ink: #444444;
    --ink-light: #4c4c4c;
    --rule: #5a5a5a;
    --shadow: rgba(0,0,0,0.55);
  }
  * { margin: 0; padding: 0; box-sizing: border-box; }
  html, body {
    width: 1200px; height: 1000px; overflow: hidden;
    background: var(--stage);
    font-family: "Varela Round", Arial, sans-serif;
  }
  .card {
    position: absolute; left: 232px; width: 718px; height: 440px;
    background: var(--card);
    box-shadow: 0 6px 14px var(--shadow);
    overflow: hidden;
    color: var(--ink);
  }
  .card--front { top: 12px; }
  .card--back { top: 509px; }
  .card__bands { position: absolute; inset: 0; width: 718px; height: 440px; }
  .card__bands polygon { fill: var(--band); stroke: var(--band-edge); stroke-width: 2; }
  .text { position: absolute; white-space: nowrap; line-height: 1; }
  .embossed { text-shadow: 0 1px 1px rgba(0,0,0,0.6), 0 -1px 0 rgba(255,255,255,0.06); }

  .wordmark {
    left: 0; width: 718px; top: 112px; text-align: center;
    font-size: 80px; letter-spacing: -2px; color: var(--ink);
  }
  .front-rule { position: absolute; left: 88px; width: 528px; top: 202px; height: 2px; background: var(--rule); }
  .front-name { left: 280px; top: 220px; font-size: 22px; }
  .front-title { left: 205px; top: 255px; font-size: 22px; }

  .back-name { left: 0; width: 726px; text-align: center; top: 24px; font-size: 68px; letter-spacing: -1px; }
  .back-title { left: 238px; top: 92px; font-size: 22px; }
  .abn { left: 32px; top: 168px; font-size: 22px; }
  .services { position: absolute; left: 46px; top: 198px; list-style: none; font-size: 22px; line-height: 25.5px; }
  .back-divider { position: absolute; left: 378px; top: 150px; width: 2px; height: 186px; background: var(--rule); }
  .address { position: absolute; left: 411px; top: 187px; font-size: 22px; line-height: 34px; }
  .contact { left: 66px; top: 408px; font-size: 22px; word-spacing: 1px; }
  .contact span + span { margin-left: 24px; }
</style>
</head>
<body>
  <section class="card card--front" aria-label="Business card front">
    <svg class="card__bands" viewBox="0 0 718 440" aria-hidden="true">
      <polygon points="0,45 45,0 100,0 0,100"/>
      <polygon points="718,45 673,0 618,0 718,100"/>
      <polygon points="0,395 45,440 100,440 0,340"/>
      <polygon points="718,395 673,440 618,440 718,340"/>
    </svg>
    <div class="text wordmark">Rivo Tanza</div>
    <div class="front-rule"></div>
    <div class="text front-name embossed">Darren Pulkett</div>
    <div class="text front-title embossed">Qualified Motorcycle Technician</div>
  </section>

  <section class="card card--back" aria-label="Business card back">
    <svg class="card__bands" viewBox="0 0 718 440" aria-hidden="true">
      <polygon points="0,45 45,0 100,0 0,100"/>
      <polygon points="718,45 673,0 618,0 718,100"/>
      <polygon points="0,395 45,440 100,440 0,340"/>
      <polygon points="718,395 673,440 618,440 718,340"/>
    </svg>
    <div class="text back-name embossed">Darren Pulkett</div>
    <div class="text back-title embossed">Qualified Motorcycle Technician</div>
    <div class="text abn embossed">ABN - 61 804 392 117</div>
    <ul class="services embossed">
      <li>-Servicing</li>
      <li>-Repairs</li>
      <li>-All makes/models</li>
      <li>-Weekends by appt.</li>
      <li>-Pick-up/delivery available</li>
    </ul>
    <div class="back-divider"></div>
    <div class="address embossed">Address : 17 Bellbrook<br>Lane, Williamstown,<br>SA</div>
    <div class="text contact embossed"><span>Tel. : 0471 582 930</span><span>Email : rivotanza@quillmail.example</span></div>
  </section>
</body>
</html>
```